Create 6 animated banners for makerting promotion

Create 6 animated banners similar to the example provided

Banner size needed

1 x 300x250
1 x 160x600
1 x 468x60
1 x 728x90
1 x 120x600
1 x 200x200

Text to be displayed:

intro screen: Trovaspark.com
animation > screen 1: The Most Refined Ad Serving Platform (pause 1.5 seconds)
animation > screen 2: Publishers - Get The Highest CPM Rates! (pause 1.5 seconds)
animation > screen 3: Advertisers - Get The Highest ROI! (pause 1.5 seconds)
animation > screen 4: Simple Dashboard (pause 1.5 seconds)
animation > screen 5: Profit From Top Quality Traffic (pause 1.5 seconds)
animation > screen 6: Account Managers Available To Help You Succeed (pause 1.5 seconds)
animation > screen 7: Click Here To Register (pause 1.5 seconds)
animation > screen 8: Trovaspark.com (pause 1.5 seconds)

background color: #0795d3

image provided must be animated gif

Attracted file with logo and sample banner
trovaspark.com logo font is Blender Pro Heavy

Target Market(s)

professional marketers, advertisers and publishers

Industry/Entity Type

Advertising

Font styles to use
Sans Serif

Requirements
Must have
• requirement text provided on description
• image must be animated gif
Nice to have
• slick animation
Should not have
• end image size should not be over 500kb

```html
<!DOCTYPE html>
<html lang="en">
<head>
<meta charset="utf-8">
<title>Trovaspark.com – 300x250 banner storyboard</title>
<link rel="stylesheet" href="https://fonts.googleapis.com/css2?family=Cabin:wght@500&display=swap">
<style>
  :root {
    --brand-blue: #0795d3;
    --canvas-white: #ffffff;
    --text-white: #ffffff;
  }
  * { margin: 0; padding: 0; box-sizing: border-box; }
  html, body {
    width: 1200px;
    height: 1000px;
    overflow: hidden;
    background: var(--canvas-white);
  }
  .storyboard {
    position: relative;
    width: 1200px;
    height: 1000px;
    font-family: "Cabin", "Gill Sans", sans-serif;
    font-weight: 500;
  }
  .frame {
    position: absolute;
    width: 300px;
    height: 250px;
    background: var(--brand-blue);
    overflow: hidden;
  }
  .col-1 { left: 116px; }
  .col-2 { left: 450px; }
  .col-3 { left: 784px; }
  .row-1 { top: 65px; }
  .row-2 { top: 381px; }
  .row-3 { top: 685px; }

  .tagline {
    position: absolute;
    width: 300px;
    text-align: center;
    color: var(--text-white);
    font-size: 20px;
    line-height: 28px;
    white-space: nowrap;
  }
  .audience-label {
    position: absolute;
    height: 29px;
    background: var(--text-white);
    color: var(--brand-blue);
    font-size: 20px;
    line-height: 29px;
    text-align: center;
    white-space: nowrap;
  }
  .is-fading { opacity: 0.75; }
  .is-faint { opacity: 0.4; }
</style>
</head>
<body>
  <main class="storyboard">
    <section class="frame row-1 col-1" aria-label="Frame 1: blank intro"></section>

    <section class="frame row-1 col-2">
      <p class="tagline is-fading" style="left:0;top:42px;">The Most Refined<br>Ad Serving Platform</p>
    </section>

    <section class="frame row-1 col-3">
      <span class="audience-label is-faint" style="left:83px;top:10px;width:135px;">PUBLISHERS</span>
      <p class="tagline is-fading" style="left:0;top:145px;">The Most Refined<br>Ad Serving Platform</p>
    </section>

    <section class="frame row-2 col-1">
      <span class="audience-label" style="left:83px;top:112px;width:135px;">PUBLISHERS</span>
      <p class="tagline is-fading" style="left:0;top:185px;">Get The Highest<br>CPM Rates!</p>
    </section>

    <section class="frame row-2 col-2">
      <span class="audience-label" style="left:83px;top:102px;width:135px;">PUBLISHERS</span>
      <p class="tagline" style="left:0;top:140px;">Get The Highest<br>CPM Rates!</p>
    </section>

    <section class="frame row-2 col-3">
      <span class="audience-label" style="left:13px;top:75px;width:135px;">PUBLISHERS</span>
      <p class="tagline" style="left:74px;top:116px;">Get The Highest<br>CPM Rates!</p>
    </section>

    <section class="frame row-3 col-1">
      <span class="audience-label" style="left:-92px;top:75px;width:135px;">PUBLISHERS</span>
      <p class="tagline" style="left:191px;top:117px;">Get The Highest<br>CPM Rates!</p>
    </section>

    <section class="frame row-3 col-2">
      <span class="audience-label" style="left:72px;top:87px;width:151px;">ADVERTISERS</span>
      <p class="tagline" style="left:0;top:133px;">Get The Highest ROI!</p>
    </section>

    <section class="frame row-3 col-3">
      <span class="audience-label" style="left:192px;top:87px;width:151px;">ADVERTISERS</span>
      <p class="tagline" style="left:-125px;top:133px;">Get The Highest ROI!</p>
    </section>
  </main>
</body>
</html>
```